National Networking/Telecommunications Company needs a new packaging (bag) design

We are currently going through a re-branding stage and need to create new packaging for all of our material.

We need a complete redesign of our current packaging (which is in various sizes). I have attached the current die-lines/knife for one of our bags.

- VORLENT logos to be changed to our PALUXO logo (attached)
- PALUXO logo to be modified, so it simply says the word PALUXO with the tick image on the end. Please remove all other writing (GRANULAR SYSTEMS & FRESH CHOICE, REMARKABLE WORTH) removed from the logo. Once this has been removed, please resize the word PALUXO, so it fits nicely beside the tick logo.
- Please remove all references to VORLENT websites, and replace with www.paluxo.com.au
- Remove "Network, Computer and Audio Video Connectivity Solutions"
- Keeping the logos that say "Lifetime Warranty" and "100% Tested and Certified", open to different ideas on how to portray them on the bag.
- Our main company colours are red, blue & silver. We're open to all designs. Packaging needs to STAND OUT, without looking cheap. Needs to still look professional and classy.
- The inside backing of the bag is to be white in colour.

I have attached our new cable box design, if that helps with keeping the colours the same.

Target Market(s)

Electrical wholesalers (who stock this product), IT/System Integrators, Installers

Industry/Entity Type

Telecommunications

Font styles to use
Sans Serif

Requirements
Must have
• Our company colours (blue, red, white/silver)
Nice to have
• Overall design needs to be simplistic, yet elegant and professional.
Should not have
• Should not have the word VORLENT anywhere

```html
<!DOCTYPE html>
<html lang="en">
<head>
<meta charset="utf-8">
<title>PALUXO Hang Bag Packaging</title>
<link rel="stylesheet" href="https://fonts.googleapis.com/css2?family=Montserrat:wght@500&family=Exo+2:wght@600&display=swap">
<style>
  :root {
    --stage: #d2d2d2;
    --navy: #12143a;
    --white: #ffffff;
    --silver: #b8bcc3;
    --red: #e3222b;
    --dim-line: #3a7cc8;
    --dim-text: #6b6b6b;
    --die-line: #7a7a7a;
  }
  html, body {
    margin: 0;
    padding: 0;
    width: 1200px;
    height: 2429px;
    overflow: hidden;
    background: var(--stage);
  }
  .canvas {
    position: relative;
    width: 1200px;
    height: 2429px;
  }
  .dimensions {
    position: absolute;
    left: 0;
    top: 0;
    width: 1200px;
    height: 1100px;
  }
  .dimensions line { stroke: var(--dim-line); stroke-width: 1.4; }
  .dimensions text {
    font-family: "Montserrat", sans-serif;
    font-size: 13px;
    fill: var(--dim-text);
  }
  .header-card {
    position: absolute;
    left: 353px;
    top: 146px;
    width: 551px;
    height: 165px;
  }
  .header-card rect, .header-card line, .header-card path {
    stroke: var(--die-line);
    stroke-width: 1.2;
    fill: var(--white);
  }
  .front-panel {
    position: absolute;
    background: var(--white);
    overflow: hidden;
  }
  .front-panel.bag { left: 353px; top: 311px; width: 551px; height: 713px; outline: 1px solid var(--die-line); }
  .front-panel.box { left: 321px; top: 1280px; width: 559px; height: 1004px; }
  .diamond { position: absolute; inset: 0; width: 100%; height: 100%; }
  .diamond polygon { fill: var(--navy); }
  .brand {
    position: absolute;
    left: 0;
    right: 0;
    display: flex;
    justify-content: center;
    align-items: center;
    gap: 16px;
  }
  .brand-name {
    font-family: "Montserrat", sans-serif;
    font-weight: 500;
    font-size: 58px;
    letter-spacing: 3px;
    color: var(--silver);
    line-height: 1;
  }
  .brand-mark {
    width: 26px;
    height: 26px;
    border-radius: 50%;
    background: var(--red);
  }
  .web-address {
    position: absolute;
    left: 0;
    right: 40px;
    text-align: center;
    font-family: "Exo 2", sans-serif;
    font-weight: 600;
    font-size: 19px;
    letter-spacing: 3px;
    color: var(--red);
  }
  .seals {
    position: absolute;
    left: 0;
    right: 0;
    display: flex;
    justify-content: center;
    gap: 28px;
  }
  .seal {
    width: 92px;
    height: 92px;
    border-radius: 50%;
  }
  .seal.warranty { background: var(--white); }
  .seal.tested { border: 2px solid var(--white); box-sizing: border-box; }
</style>
</head>
<body>
<main class="canvas">

  <svg class="dimensions" viewBox="0 0 1200 1100" aria-hidden="true">
    <line x1="356" y1="115" x2="899" y2="115"/>
    <text x="602" y="119" text-anchor="middle" style="fill:var(--dim-text)">150mm</text>
    <line x1="318" y1="146" x2="318" y2="1024"/>
    <text x="318" y="585" text-anchor="middle" transform="rotate(-90 318 585)">240mm</text>
    <line x1="917" y1="146" x2="917" y2="204"/>
    <text x="922" y="180">15mm</text>
    <line x1="944" y1="204" x2="944" y2="272"/>
    <text x="925" y="238">20mm</text>
    <line x1="982" y1="146" x2="982" y2="308"/>
    <text x="960" y="260">45mm</text>
    <line x1="917" y1="316" x2="917" y2="612"/>
    <text x="910" y="457">82mm</text>
  </svg>

  <svg class="header-card" viewBox="0 0 551 165" aria-hidden="true">
    <rect x="0.5" y="0.5" width="550" height="164"/>
    <line x1="0" y1="57" x2="551" y2="57"/>
    <path d="M226 127 h30 a8 8 0 0 1 8 -8 h22 a8 8 0 0 1 8 8 h30 a7 7 0 0 1 0 14 h-98 a7 7 0 0 1 0 -14 z"/>
  </svg>

  <section class="front-panel bag">
    <svg class="diamond" viewBox="0 0 551 713" preserveAspectRatio="none" aria-hidden="true">
      <polygon points="275,10 551,286 551,437 275,713 0,437 0,286"/>
    </svg>
    <div class="brand" style="top:314px">
      <span class="brand-name">PALUXO</span>
      <span class="brand-mark"></span>
    </div>
    <div class="web-address" style="top:384px">www.paluxo.com.au</div>
    <div class="seals" style="top:509px">
      <span class="seal warranty"></span>
      <span class="seal tested"></span>
    </div>
  </section>

  <section class="front-panel box">
    <svg class="diamond" viewBox="0 0 559 1004" preserveAspectRatio="none" aria-hidden="true">
      <polygon points="280,22 559,301 559,725 280,1004 0,725 0,301"/>
    </svg>
    <div class="brand" style="top:448px">
      <span class="brand-name">PALUXO</span>
      <span class="brand-mark"></span>
    </div>
    <div class="web-address" style="top:540px">www.paluxo.com.au</div>
    <div class="seals" style="top:707px">
      <span class="seal warranty"></span>
      <span class="seal tested"></span>
    </div>
  </section>

</main>
</body>
</html>
```